Vantrell Law Letterhead

We need a new letterhead design for a Law Firm. The address for the law firm is 4817 Larkspur Boulevard, Suite 250, Houston, Texas 77342. Phone Number: 832-619-3057; Fax Number: 832-407-1694. The logo is uploaded to the project.

```html
<!DOCTYPE html>
<html lang="en">
<head>
<meta charset="utf-8">
<title>Vantrell Law Letterhead</title>
<link href="https://fonts.googleapis.com/css2?family=Cinzel:wght@500&family=Arimo&display=swap" rel="stylesheet">
<style>
  :root {
    --brand-red: #e31b23;
    --brand-navy: #1f2f66;
    --watermark: #eef0f4;
    --footer-text: #4d4d4d;
    --icon-grey: #6b6b6b;
    --paper: #ffffff;
  }
  * { margin: 0; padding: 0; box-sizing: border-box; }
  html, body { width: 848px; height: 1200px; overflow: hidden; background: var(--paper); }
  .letterhead { position: relative; width: 848px; height: 1200px; background: var(--paper); }
  .frame-accents { position: absolute; inset: 0; width: 848px; height: 1200px; }
  .brand {
    position: absolute; top: 62px; left: 0; width: 848px;
    display: flex; justify-content: center; align-items: center; gap: 18px;
  }
  .brand-mark { width: 96px; height: 96px; border-radius: 50%; background: var(--brand-navy); flex: none; }
  .brand-text { display: flex; flex-direction: column; align-items: center; width: 258px; }
  .brand-name {
    font-family: "Cinzel", serif; font-weight: 500; font-size: 34px;
    color: var(--brand-navy); line-height: 1; letter-spacing: 0.5px; white-space: nowrap;
  }
  .brand-rule { width: 254px; height: 1px; background: var(--brand-red); margin: 14px 0 12px; }
  .brand-tagline {
    font-family: "Cinzel", serif; font-weight: 500; font-size: 9.5px; letter-spacing: 1.9px;
    color: var(--brand-red); white-space: nowrap;
  }
  .watermark {
    position: absolute; left: 215px; top: 382px; width: 468px; height: 468px;
    border-radius: 50%; background: var(--watermark);
  }
  .contact {
    position: absolute; top: 1106px; left: 0; width: 848px;
    font-family: "Arimo", sans-serif; font-size: 15px; color: var(--footer-text);
  }
  .contact-item { position: absolute; display: flex; align-items: flex-start; gap: 10px; line-height: 24px; }
  .contact-item svg { flex: none; fill: var(--icon-grey); }
  .contact-address { left: 79px; }
  .contact-phone { left: 391px; top: 2px; }
  .contact-fax { left: 599px; top: 2px; }
  .contact-phone svg, .contact-fax svg { margin-top: 3px; }
</style>
</head>
<body>
<main class="letterhead">
  <svg class="frame-accents" viewBox="0 0 848 1200" aria-hidden="true">
    <polygon fill="var(--brand-red)" points="0,0 66,0 0,66"/>
    <polygon fill="var(--brand-red)" points="80,0 848,0 848,19 78,19 0,96 0,78"/>
    <polygon fill="var(--brand-red)" points="0,1181 770,1181 848,1104 848,1122 789,1181 848,1181 848,1200 0,1200"/>
    <polygon fill="var(--brand-red)" points="848,1134 848,1200 783,1200"/>
  </svg>

  <header class="brand">
    <div class="brand-mark"></div>
    <div class="brand-text">
      <div class="brand-name">Vantrell Law</div>
      <div class="brand-rule"></div>
      <div class="brand-tagline">DEDICATED COUNSEL FOR EVERY CLIENT</div>
    </div>
  </header>

  <div class="watermark" aria-hidden="true"></div>

  <footer class="contact">
    <div class="contact-item contact-address">
      <svg width="20" height="28" viewBox="0 0 20 28" aria-hidden="true">
        <path d="M10 1a8 8 0 0 0-8 8c0 6 8 13 8 13s8-7 8-13a8 8 0 0 0-8-8zm0 11a3.2 3.2 0 1 1 0-6.4 3.2 3.2 0 0 1 0 6.4z"/>
        <ellipse cx="10" cy="25" rx="9" ry="2.2" fill="none" stroke="var(--icon-grey)" stroke-width="1.5"/>
      </svg>
      <div>4817 Larkspur Boulevard<br>Suite 250, Houston, Texas 77342</div>
    </div>
    <div class="contact-item contact-phone">
      <svg width="16" height="18" viewBox="0 0 24 24" aria-hidden="true">
        <path d="M6.6 10.8a15 15 0 0 0 6.6 6.6l2.2-2.2a1 1 0 0 1 1-.25 11.4 11.4 0 0 0 3.6.6 1 1 0 0 1 1 1V20a1 1 0 0 1-1 1A17 17 0 0 1 3 4a1 1 0 0 1 1-1h3.5a1 1 0 0 1 1 1c0 1.25.2 2.45.6 3.6a1 1 0 0 1-.25 1z"/>
      </svg>
      <div>832-619-3057</div>
    </div>
    <div class="contact-item contact-fax">
      <svg width="18" height="18" viewBox="0 0 24 24" aria-hidden="true">
        <path d="M7 2h10v6H7z M3 9h18a1 1 0 0 1 1 1v10a1 1 0 0 1-1 1H3a1 1 0 0 1-1-1V10a1 1 0 0 1 1-1zm4 6h10v2H7z"/>
      </svg>
      <div>832-407-1694</div>
    </div>
  </footer>
</main>
</body>
</html>
```